Kyvex brochure for corporate sector

Our company provides audio visual solutions to the corporate and government markets across Australia. Interactive touch screens are popular in schools and education sectors but are slow to adopt in the corporate market. We wish to create an attention-grabbing A4 single sided colour brochure to promote a state-of-the-art large-format touchscreen product to the financial sector - more specifically for financial planners, board meeting etc. These are available on 55",65",70" and 84" sizes making them ideal for meetings to interact with customers while impressing them with technology.
We have attached a brochure that details the products impressive capability, whcih needs to be summed up in just an A4 brochure.
Key features to include....
-HD resolution of 1920 x 1080
-Screen sizes of 55,65,70 and 84"
-Capture ideas/notes/ direct to internal memory or USB
-Annotate over presentations and save/email/share
-20-point touch (for multiple users at the same time)
-inbuilt Nimbus OS-(brouse the web, access Apps)
-Anti-scratch/Anti-glare screen
-Q-Flow wifi for sharing direct from smartphones/tablets
-Multiple inputs for other devices

Special Offer
Fully installed 55” kyvex with wall bracket, USB/VGA/HDMI wall plate and all cabling from only $85.00 inc GST per week for 24 months.(conditions apply)

Design should include company logo, carry across our "BLUE" corporate feel. and contact details (phone, email and web)

Images and previous brochure attached for corporate feel etc.
We feel that some stock images might be required to convey the touchscreen being used in a corporate/professional environment might be required, happy to take your advise on this and purchase if required.

Target Market(s)

Corporate, finance and government

Industry/Entity Type

Government

Font styles to use
Serif
Sans Serif

Colors
3377b5
0255a3

Requirements
Must have
• Be attention-grabbing using the technology and simplicity of the product to gain interest to prospective buyers interested in showing their customers or staff they are an industry leader by adopting technology. Must carry the same Tolk group corporate feel as previous brochure (attached as sample).
Should not have
• Be cluttered and confusing. Not look like the existing kyvex brochure which is targeted towards education and schools. This product has enormous potential for the business, corporate and government sectors.

```html
<!DOCTYPE html>
<html lang="en">
<head>
<meta charset="utf-8">
<title>Kyvex – Professional Audio Visual Solutions</title>
<link href="https://fonts.googleapis.com/css2?family=Oswald:wght@500;600&family=Roboto+Condensed:wght@700&family=Orbitron:wght@400&family=Lato:wght@400&display=swap" rel="stylesheet">
<style>
  :root{
    --ink:#232a33;
    --teal:#1a9cc4;
    --sky:#5aaee0;
    --sky-deep:#3f9ad2;
    --heading:#3a9fd6;
    --paper:#ffffff;
    --page:#eef0f2;
    --body-text:#2a2f36;
  }
  html,body{margin:0;padding:0;width:1200px;height:1200px;overflow:hidden;background:var(--page);}
  .flyer{
    position:absolute;left:194px;top:30px;width:961px;height:1350px;
    background:var(--paper);transform:scale(0.8444);transform-origin:0 0;overflow:hidden;
  }
  .shapes{position:absolute;left:0;top:0;}
  .brand{
    position:absolute;right:17px;top:212px;
    font-family:"Lato",sans-serif;font-size:33px;color:var(--ink);letter-spacing:-0.3px;
  }
  .title{position:absolute;left:588px;width:360px;text-align:center;line-height:1;white-space:nowrap;}
  .title-professional{top:392px;font-family:"Oswald",sans-serif;font-weight:600;font-size:56px;color:var(--teal);letter-spacing:-0.5px;}
  .title-av{top:452px;font-family:"Oswald",sans-serif;font-weight:600;font-size:56px;color:#fff;}
  .title-solutions{top:512px;font-family:"Orbitron",sans-serif;font-size:44px;color:var(--teal);letter-spacing:2px;}
  .section-heading{
    position:absolute;left:38px;margin:0;
    font-family:"Roboto Condensed",sans-serif;font-weight:700;font-size:30px;color:var(--heading);line-height:1;
  }
  .features-heading{top:642px;}
  .offer-heading{top:957px;}
  .features{
    position:absolute;left:40px;top:684px;margin:0;padding:0;list-style:none;
    font-family:"Lato",sans-serif;font-size:16px;color:var(--body-text);
  }
  .features li{height:27.2px;line-height:24px;padding-left:15px;position:relative;}
  .features li::before{content:"";position:absolute;left:1px;top:9px;width:6px;height:6px;border-radius:50%;background:var(--teal);}
  .offer-copy{
    position:absolute;left:36px;top:1036px;font-family:"Roboto Condensed",sans-serif;font-weight:700;color:#fff;
  }
  .offer-copy .lead{font-size:31px;line-height:34px;}
  .offer-copy .detail{font-size:22px;line-height:27px;}
  .hl{color:var(--heading);}
  .call{position:absolute;left:36px;top:1170px;font-size:44px;line-height:1;color:#fff;white-space:nowrap;}
  .call-label{font-family:"Roboto Condensed",sans-serif;font-weight:700;color:var(--heading);}
  .call-number{font-family:"Lato",sans-serif;margin-left:6px;}
  .price{position:absolute;font-family:"Roboto Condensed",sans-serif;font-weight:700;line-height:1;color:var(--ink);white-space:nowrap;}
  .price-amount{left:395px;top:1006px;font-family:"Oswald",sans-serif;font-weight:600;font-size:56px;color:var(--heading);}
  .price-gst{left:431px;top:1074px;font-size:36px;}
  .price-week{left:468px;top:1111px;font-size:36px;color:var(--heading);}
  .price-term{left:491px;top:1148px;font-size:36px;}
  .footer{
    position:absolute;left:0;top:1230px;width:961px;height:90px;
    font-family:"Lato",sans-serif;font-size:16px;color:#fff;
  }
  .footer-item{position:absolute;top:36px;display:flex;align-items:center;gap:10px;white-space:nowrap;}
  .footer-item svg{flex:none;}
</style>
</head>
<body>
<div class="flyer">
  <svg class="shapes" width="961" height="1350" viewBox="0 0 961 1350">
    <defs>
      <linearGradient id="officeTone" x1="0" y1="0" x2="1" y2="1">
        <stop offset="0" stop-color="#d9e8f3"/>
        <stop offset="0.55" stop-color="#a9c6dc"/>
        <stop offset="1" stop-color="#e4ebf1"/>
      </linearGradient>
      <linearGradient id="touchTone" x1="0" y1="0" x2="0" y2="1">
        <stop offset="0" stop-color="#9fc1dd"/>
        <stop offset="1" stop-color="#2f6aa6"/>
      </linearGradient>
      <linearGradient id="screenTone" x1="0" y1="0" x2="1" y2="1">
        <stop offset="0" stop-color="#173a63"/>
        <stop offset="1" stop-color="#6b7a88"/>
      </linearGradient>
    </defs>

    <g role="img" aria-label="Businesswoman seated with a laptop in a bright office, cloud and device icons floating above">
      <polygon points="0,0 752,0 479,576 0,576" fill="url(#officeTone)"/>
    </g>
    <polygon points="756,0 782,0 497,600 471,600" fill="var(--teal)"/>
    <rect x="0" y="580" width="486" height="20" fill="var(--teal)"/>
    <polygon points="624,332 961,332 961,600 497,600" fill="var(--ink)"/>

    <polygon points="508,600 961,600 961,1262" fill="var(--sky)"/>
    <polygon points="495,600 508,600 961,1262 961,1290" fill="var(--ink)"/>
    <polygon points="490,600 500,600 950,1262 940,1262" fill="var(--ink)"/>

    <rect x="496" y="670" width="236" height="224" fill="var(--ink)"/>
    <rect x="502" y="676" width="224" height="212" fill="var(--teal)"/>
    <rect x="508" y="682" width="212" height="200" fill="#fff"/>
    <g role="img" aria-label="Hand touching a glowing interactive screen over a city skyline">
      <rect x="516" y="690" width="196" height="184" fill="url(#touchTone)"/>
    </g>
    <rect x="648" y="933" width="226" height="211" fill="var(--ink)"/>
    <rect x="654" y="939" width="214" height="199" fill="var(--teal)"/>
    <rect x="660" y="945" width="202" height="187" fill="#fff"/>
    <g role="img" aria-label="Businesswoman with a tablet in front of a large digital display">
      <rect x="667" y="952" width="188" height="173" fill="url(#screenTone)"/>
    </g>

    <polygon points="0,1005 342,1005 496,1230 0,1230" fill="var(--ink)"/>
    <rect x="0" y="1230" width="961" height="90" fill="var(--ink)"/>
  </svg>

  <div class="brand">tolk group systems</div>

  <div class="title title-professional">PROFESSIONAL</div>
  <div class="title title-av">AUDIO VISUAL</div>
  <div class="title title-solutions">SOLUTIONS</div>

  <h2 class="section-heading features-heading">Key features to include</h2>
  <ul class="features">
    <li>HD resolution of 1920 x 1080</li>
    <li>Screen sizes of 55,65,70 and 84"</li>
    <li>Capture ideas/notes/ direct to internal memory or USB</li>
    <li>Annotate over presentations and save/email/share</li>
    <li>20-point touch (for multiple users at the same time)</li>
    <li>inbuilt Nimbus OS-(brouse the web, access Apps)</li>
    <li>Anti-scratch/Anti-glare screen</li>
    <li>Q-Flow wifi for sharing direct from smartphones/tablets</li>
    <li>Multiple inputs for other devices</li>
  </ul>

  <h2 class="section-heading offer-heading">Special Offer</h2>
  <div class="offer-copy">
    <div class="lead"><span class="hl">Fully installed 55”</span> kyvex</div>
    <div class="detail">with wall bracket, <span class="hl">USB/VGA/HDMI</span></div>
    <div class="detail">wall plate and all cabling from only</div>
  </div>
  <div class="call"><span class="call-label">CALL</span><span class="call-number">02 9000 4100</span></div>

  <div class="price price-amount">$85.00</div>
  <div class="price price-gst">inc GST per</div>
  <div class="price price-week">week for</div>
  <div class="price price-term">24 months</div>

  <div class="footer">
    <div class="footer-item" style="left:39px;">ABN :00 000 000 000</div>
    <div class="footer-item" style="left:245px;">
      <svg width="22" height="18" viewBox="0 0 22 18"><path d="M2 7c0-3 4-5 9-5s9 2 9 5l-4 1-1-2H7L6 8z" fill="var(--sky)"/><rect x="5" y="9" width="12" height="8" rx="2" fill="var(--sky)"/></svg>
      <span>02 9000 4199</span>
    </div>
    <div class="footer-item" style="left:448px;">
      <svg width="16" height="14" viewBox="0 0 16 14"><rect x="0" y="2" width="16" height="12" rx="1" fill="var(--sky)"/><path d="M1 3l7 6 7-6" stroke="var(--ink)" stroke-width="1.4" fill="none"/></svg>
      <span>hello@tolkgroup.example</span>
    </div>
    <div class="footer-item" style="left:685px;">
      <svg width="18" height="18" viewBox="0 0 18 18"><circle cx="9" cy="9" r="8" fill="var(--sky)"/><path d="M1 9h16M9 1c-4 4-4 12 0 16M9 1c4 4 4 12 0 16" stroke="var(--ink)" stroke-width="1.2" fill="none"/></svg>
      <span>www.tolkgroup.example</span>
    </div>
  </div>
</div>
</body>
</html>
```